V9 Web Design Project

New company website for Intel cyber security company.

Style should be cool, but remain appropriate for very serious subject matter and audience.

Target Market(s)

Target audience is government and the military

Navigation needs to include:
- About Us
- Services
- Careers
- Contact Us
- Contracts

As well as 2 feature areas - use "Technology Integration" and "Case Study" as the supporting headlines.

Industry/Entity Type

Security

Font styles to use
Sans Serif

Colors

Designer to choose colors to be used in the design.

Requirements
Must have
• Mountain imagery and theme.

Use logo attached.

New Tagline - "Securing the Continuum"
Nice to have
• Supporting imagery could include photos representative of security - avoid cliches.
Should not have
• Needs to be serious not frivolous

```html
<!DOCTYPE html>
<html lang="en">
<head>
<meta charset="utf-8">
<title>V9 Group — Securing the Continuum</title>
<link href="https://fonts.googleapis.com/css2?family=Arimo:wght@400;700&family=Didact+Gothic&family=Montserrat:wght@400;500&family=Open+Sans:wght@400;600&display=swap" rel="stylesheet">
<style>
  :root{
    --navy:#1f3f7d;
    --brand-blue:#2d5796;
    --link-blue:#2c5aa0;
    --footer-dark:#0b1a35;
    --copyright-blue:#2a4f8e;
    --ink:#1c1c1c;
    --muted:#555a66;
    --white:#ffffff;
  }
  *{margin:0;padding:0;box-sizing:border-box}
  html,body{width:933px;height:1200px;overflow:hidden;background:var(--white)}
  body{position:relative;font-family:"Didact Gothic",sans-serif;color:var(--ink)}
  .abs{position:absolute}

  /* Hero */
  .hero{left:0;top:0;width:933px;height:326px;
    background:linear-gradient(180deg,#8c9aa3 0%,#a6b0b3 30%,#6d7a80 55%,#2c3638 80%,#1a2224 100%)}
  .hero-title{left:282px;top:138px;width:370px;height:41px;background:rgba(60,60,60,.55);
    color:#fff;font-family:"Montserrat",sans-serif;font-size:28px;text-align:center;line-height:41px;white-space:nowrap}
  .hero-sub{left:264px;top:181px;width:406px;height:62px;background:rgba(40,40,40,.45);
    color:#eee;font-family:"Montserrat",sans-serif;font-size:16.5px;text-align:center;line-height:24px;padding-top:6px}
  .dots{left:448px;top:311px;display:flex;gap:4px}
  .dots span{width:6px;height:6px;border-radius:50%;background:#fff}
  .dots span.active{background:#8fb6d6}

  /* Header */
  .header{left:134px;top:0;width:667px;height:62px;background:rgba(255,255,255,.96);box-shadow:0 1px 4px rgba(0,0,0,.3)}
  .brand{left:10px;top:11px;display:flex;align-items:center;gap:11px}
  .brand-mark{width:43px;height:43px;background:var(--navy)}
  .brand-name{font-family:"Arimo",sans-serif;font-size:25px;color:var(--navy);letter-spacing:.5px;white-space:nowrap}
  .social{left:599px;top:5px;display:flex;gap:7px}
  .social span{width:16px;height:16px;border-radius:2px}
  .nav-item{top:40px;height:22px;line-height:22px;font-family:"Arimo",sans-serif;font-size:10px;color:#333;
    text-decoration:none;white-space:nowrap;transform:translateX(-50%)}
  .nav-item.current{background:var(--brand-blue);color:#fff;width:44px;text-align:center}

  /* Services */
  .services{left:0;top:326px;width:933px;height:296px;background:linear-gradient(180deg,#f4f6fa,#e8ecf4)}
  .services h2{position:absolute;left:0;width:933px;top:28px;text-align:center;
    font-family:"Arimo",sans-serif;font-weight:400;font-size:28px;color:var(--link-blue)}
  .card-hl{left:266px;top:406px;width:137px;height:192px;background:#fff;box-shadow:0 1px 6px rgba(0,0,0,.1)}
  .service{width:130px;top:430px;text-align:center}
  .service svg{display:block;margin:0 auto;height:40px}
  .service h3{margin-top:34px;font-family:"Arimo",sans-serif;font-weight:400;font-size:13px;color:var(--link-blue);white-space:nowrap}
  .service p{margin-top:4px;font-family:"Arimo",sans-serif;font-size:8.4px;line-height:11px;color:#111;white-space:nowrap}
  .btn{display:inline-block;margin-top:16px;width:68px;height:18px;line-height:16px;border:1px solid var(--brand-blue);
    font-family:"Arimo",sans-serif;font-size:8px;color:var(--brand-blue);white-space:nowrap}
  .btn.solid{background:var(--brand-blue);color:#fff}

  /* Welcome */
  .welcome{left:134px;top:660px;width:668px}
  .welcome h2{font-family:"Arimo",sans-serif;font-weight:400;font-size:25px;color:var(--link-blue);white-space:nowrap}
  .welcome p{margin-top:14px;font-size:9.1px;line-height:14.6px;color:var(--muted)}
  .welcome p+p{margin-top:14px}

  /* News */
  .news{left:0;top:834px;width:933px;height:168px;background:linear-gradient(90deg,#2a5096,#3461a8 60%,#2d5597)}
  .news h2{position:absolute;left:146px;top:36px;font-family:"Open Sans",sans-serif;font-weight:600;font-size:22px;color:#fff;white-space:nowrap}
  .news .kicker{position:absolute;left:146px;top:68px;font-family:"Open Sans",sans-serif;font-size:13px;color:#fff;white-space:nowrap}
  .news-photo{left:349px;top:28px;width:112px;height:112px;border-radius:50%;border:3px solid #b7c6dc;
    background:radial-gradient(circle at 50% 50%,#c93a3a 0%,#7a2a4a 35%,#2a4a8a 75%)}
  .arrow{top:76px}
  .avatar{left:496px;top:38px;width:26px;height:26px;background:#9a7a6a;border:1px solid #fff}
  .post-title{left:533px;top:36px;font-family:"Open Sans",sans-serif;font-weight:600;font-size:12px;color:#fff;white-space:nowrap}
  .post-date{left:534px;top:52px;font-family:"Open Sans",sans-serif;font-size:9.5px;color:#fff;white-space:nowrap}
  .post-body{left:496px;top:75px;width:285px;font-family:"Open Sans",sans-serif;font-size:10.5px;line-height:13px;color:#fff}

  /* Footer */
  .footer{left:0;top:1002px;width:933px;height:154px;background:var(--footer-dark)}
  .footer h4{font-family:"Montserrat",sans-serif;font-weight:500;font-size:11px;letter-spacing:.6px;color:#fff}
  .footer ul{list-style:none;margin-top:10px;font-family:"Open Sans",sans-serif;font-size:8.6px;line-height:13.3px;color:#fff}
  .footer p{margin-top:10px;font-family:"Open Sans",sans-serif;font-size:8.6px;line-height:14.8px;color:#fff}
  .col-nav{left:141px;top:20px}
  .col-loc{left:334px;top:20px;width:200px}
  .col-news{left:591px;top:20px;width:205px}
  .col-news p{line-height:10px}
  .subscribe{margin-top:9px;display:flex;height:16px}
  .subscribe .field{width:141px;background:#fff;font-family:"Open Sans",sans-serif;font-size:7.5px;color:#666;line-height:16px;padding-left:6px}
  .subscribe .go{width:60px;background:var(--brand-blue);color:#fff;font-family:"Open Sans",sans-serif;font-weight:600;font-size:8.5px;text-align:center;line-height:16px}
  .copyright{left:0;top:1156px;width:933px;height:44px;background:var(--copyright-blue);
    text-align:center;line-height:44px;font-family:"Open Sans",sans-serif;font-size:8.8px;color:#fff}
</style>
</head>
<body>

<div class="abs hero" role="img" aria-label="Misty mountain lake landscape at dusk"></div>
<div class="abs hero-title">Securing the Continuum</div>
<div class="abs hero-sub">Lorem Ipsum is simply dummy text of the<br>printing and typesetting industry.</div>
<div class="abs dots"><span></span><span class="active"></span><span></span><span></span></div>

<header class="abs header">
  <div class="abs brand"><span class="brand-mark"></span><span class="brand-name">V9 GROUP</span></div>
  <div class="abs social">
    <span style="background:#3b5a9a"></span><span style="background:#3aa0d0"></span><span style="background:#e8822a"></span>
  </div>
</header>
<nav aria-label="Main">
  <a class="abs nav-item current" href="#" style="left:403px">Home</a>
  <a class="abs nav-item" href="#" style="left:472px">About Us</a>
  <a class="abs nav-item" href="#" style="left:545px">Services</a>
  <a class="abs nav-item" href="#" style="left:616px">Careers</a>
  <a class="abs nav-item" href="#" style="left:692px">Contact Us</a>
  <a class="abs nav-item" href="#" style="left:771px">Contracts</a>
</nav>

<section class="abs services"><h2>Our Services</h2></section>
<div class="abs card-hl"></div>

<div class="abs service" style="left:134px">
  <svg viewBox="0 0 48 40"><path d="M2 6h14l4 4h22v26H2z" fill="#1a1a1a"/><rect x="20" y="20" width="14" height="11" fill="#fff"/><path d="M23 20v-4a4 4 0 0 1 8 0v4" stroke="#fff" stroke-width="2" fill="none"/></svg>
  <h3>Lorem Ipsum</h3><p>Praesent elementum, quam<br>rhoncus ornare, turpis</p><span class="btn">READ MORE</span>
</div>
<div class="abs service" style="left:270px">
  <svg viewBox="0 0 40 40"><circle cx="20" cy="20" r="18" fill="#2d5796"/><circle cx="20" cy="17" r="4" fill="#fff"/><path d="M18 19h4l1 9h-6z" fill="#fff"/><rect x="8" y="18" width="4" height="1.5" fill="#fff"/><rect x="28" y="18" width="4" height="1.5" fill="#fff"/></svg>
  <h3>Lorem Ipsum</h3><p>Praesent elementum, qua<br>mrhoncus ornare, turpis</p><span class="btn solid">READ MORE</span>
</div>
<div class="abs service" style="left:408px">
  <svg viewBox="0 0 50 40"><rect x="2" y="6" width="46" height="32" rx="3" fill="#1a1a1a"/><rect x="17" y="2" width="16" height="7" fill="#1a1a1a"/><circle cx="14" cy="20" r="4" fill="#fff"/><path d="M7 31a7 6 0 0 1 14 0z" fill="#fff"/><rect x="25" y="17" width="17" height="2.5" fill="#fff"/><rect x="25" y="23" width="17" height="2.5" fill="#fff"/><rect x="25" y="29" width="12" height="2.5" fill="#fff"/></svg>
  <h3>Lorem Ipsum</h3><p>Praesent elementum, quam<br>rhoncus ornare, turpis</p><span class="btn">READ MORE</span>
</div>
<div class="abs service" style="left:545px">
  <svg viewBox="0 0 40 40"><circle cx="16" cy="15" r="10" fill="none" stroke="#1a1a1a" stroke-width="6" stroke-dasharray="4 3.8"/><circle cx="16" cy="15" r="8" fill="#1a1a1a"/><circle cx="16" cy="15" r="3" fill="#fff"/><circle cx="30" cy="30" r="5" fill="none" stroke="#1a1a1a" stroke-width="4" stroke-dasharray="2.5 2.2"/><circle cx="30" cy="30" r="4" fill="#1a1a1a"/><circle cx="30" cy="30" r="1.5" fill="#fff"/></svg>
  <h3>Lorem Ipsum</h3><p>Praesent elementum, quam<br>rhoncus ornare, turpis</p><span class="btn">READ MORE</span>
</div>
<div class="abs service" style="left:680px">
  <svg viewBox="0 0 48 40"><rect x="7" y="8" width="34" height="22" rx="2" fill="none" stroke="#1a1a1a" stroke-width="3"/><path d="M2 32h44l-3 4H5z" fill="#1a1a1a"/></svg>
  <h3>Lorem Ipsum</h3><p>Praesent elementum, quam<br>rhoncus ornare, turpis</p><span class="btn">READ MORE</span>
</div>

<section class="abs welcome">
  <h2>Welcome to Marlowe Accounting</h2>
  <p>Praesent sollicitudin fermentum ante, eget volutpat diam lobortis id. Praesent placerat, lacus ac ultricies interdum, ante ipsum ullamcorper dolor, id tempus neque ipsum in ipsum. Nulla facilisi. Ut luctus neque ut neque tincidunt id rutrum erat viverra. Sed suscipit, ipsum non auctor tincidunt, turpis sapien ultrices justo, in ultricies sem arcu ac eros. Nulla convallis faucibus viverra. Donec congue nunc ut ante vestibulum quis lobortis orci adipiscing.</p>
  <p>Mauris pretium vestibulum risus, at rhoncus sapien luctus ut. Nulla dapibus, est id varius dictum, tellus augue scelerisque leo, a lacinia lorem diam vel ligula. Donec at diam vel metus viverra suscipit elementum eu nulla. Proin suscipit aliquam sapien eget sagittis.</p>
</section>

<section class="abs news" aria-label="Latest news">
  <h2>Latest News</h2>
  <div class="kicker">Protection Services</div>
  <svg class="abs arrow" style="left:328px" width="10" height="14" viewBox="0 0 10 14"><path d="M8 1 2 7l6 6" stroke="#0d1f44" stroke-width="3" fill="none"/></svg>
  <div class="abs news-photo" role="img" aria-label="Close-up of a keyboard with a red information security key"></div>
  <svg class="abs arrow" style="left:472px" width="10" height="14" viewBox="0 0 10 14"><path d="M2 1l6 6-6 6" stroke="#fff" stroke-width="3" fill="none"/></svg>
  <div class="abs avatar" role="img" aria-label="Author portrait"></div>
  <div class="abs post-title">Suspendisse</div>
  <div class="abs post-date">06-03-2013</div>
  <div class="abs post-body">The Summit Group Announces New Protective Services<br>The Summit Group is proud to announce the opening of our Protective Services Division, “Summit Protective Services….</div>
</section>

<footer class="abs footer">
  <div class="abs col-nav"><h4>NAVIGATION</h4>
    <ul><li>About</li><li>Security</li><li>Investigation</li><li>Remote Medicine</li><li>Intelligence</li><li>Training</li><li>Contact Us</li></ul>
  </div>
  <div class="abs col-loc"><h4>LOCATION</h4>
    <p>Ma. Aliquam lectus enim, convallis a tempus in, lacinia et dolor. USA<br>P: +1 555 010 0190<br>F: +1 555 010 0191<br>E: info@ridgelineconsult.com</p>
  </div>
  <div class="abs col-news"><h4>NEWSLETTER</h4>
    <p>Subscribe for our newsletters. We promise to send you only important information and to protect your privacy!</p>
    <div class="subscribe"><span class="field">Enter email</span><span class="go">Subscribe</span></div>
  </div>
</footer>
<div class="abs copyright">Copyright © Ridgeline Consultants. All rights reserved.</div>

</body>
</html>
```